Skincare Clinic specializing in treating difficult skin conditions needs a web design

We want to restructure and rehash our current webdesigns. The current ones are dated and look very old fashioned also, they are not structured well.

The current websites need to get an uplift in look and become more classy and modern with navigation ease by structuring the information into ease of access

The current web address is
www.brightlumera.com.au and
www.velorandum.com.au

We also have international Partner website which is good and we need to better than them. So this website will act as a guide to better the new site
www.tenvora-drholbrook.com

But the new site should be more inclined towards a Blue colour or Aqua marine blue orientation and it needs to be Scientific giving authenticity to the medical industry we operate in.

Attached is a webdesign framework and architecture we would want to adopt. It is a schematic diagram and you can creatively adopt based on what you want to propose.

The website needs to be coded and Should be coded in WordPress such that it helps with SEO activity and google adwords pickup.

We will need the necessary pictures and we could provide them or agree to by them from the designers source.

Target Market(s)

Patients with Skin Disease and people interested to book consultation or buy products for their Skin condition

Industry/Entity Type

Clinic

Coding

Coded - Design and coding required

Number of Pages Required

5+ page

Font styles to use
Other font styles liked:
• Use a light font denoting class.

Requirements
Must have
• Should be modern, Easy to navigate, mobile friendly and coded in wordpress
• Blue colour and should look scientific and medicinal
Nice to have
• Classy and creative
Should not have
• No Green colour or herbal look

```html
<!DOCTYPE html>
<html lang="en">
<head>
<meta charset="utf-8">
<title>Brightlumera Skin Clinic</title>
<link rel="stylesheet" href="https://fonts.googleapis.com/css2?family=Source+Sans+3:wght@300;400;600&family=Libre+Baskerville&family=Arimo:wght@400;700&display=swap">
<style>
:root{
  --aqua:#6ac8cf;
  --sky:#1aa6e0;
  --footer:#29a8e2;
  --ink:#333;
  --body:#444;
  --white:#fff;
  --line:#e2e2e2;
}
*{margin:0;padding:0;box-sizing:border-box}
html,body{width:717px;height:1200px;overflow:hidden;background:var(--white)}
body{font-family:"Source Sans 3",sans-serif;color:var(--ink)}
.page{position:relative;width:717px;height:1200px;overflow:hidden}
.abs{position:absolute}

/* header */
.promo{left:60px;top:14px;width:330px;height:74px;border:1px solid #999;background:linear-gradient(90deg,#f4f1ec,#fff 40%,#eeeae5)}
.promo-product{position:absolute;top:2px;height:68px;background:linear-gradient(180deg,#7a4a22,#3b1f0a)}
.promo-product.left{left:2px;width:58px;border-radius:6px 6px 0 0}
.promo-product.right{right:3px;width:14px;background:linear-gradient(180deg,#666,#222)}
.promo-title{position:absolute;left:73px;top:5px;font-family:"Libre Baskerville",serif;font-size:12.5px;line-height:13px;color:#3a2410}
.promo-btn{position:absolute;left:76px;top:42px;width:82px;height:22px;background:#f6f6f6;border:1px solid #ddd;font-family:"Arimo",sans-serif;font-size:9px;line-height:20px;text-align:center;color:#333}
.promo-price{position:absolute;right:22px;top:49px;font-family:"Libre Baskerville",serif;font-size:8px;line-height:10px;text-align:right;color:#3a2410}
.social{top:18px;left:535px;display:flex;gap:4px}
.social span{width:18px;height:18px;border-radius:50%;background:#ccc}
.clinic-name{left:468px;top:48px;width:190px;text-align:right;font-size:17px;font-weight:400;line-height:22px;color:var(--ink);white-space:nowrap}

/* nav */
.nav{left:0;top:102px;width:717px;height:30px;background:var(--aqua);display:flex;padding-left:58px}
.nav a{color:var(--white);text-decoration:none;font-size:9.5px;text-transform:uppercase;line-height:30px;padding:0 13px;border-right:1px solid rgba(255,255,255,.35)}
.nav a:last-child{border-right:0}

/* hero */
.hero{left:0;top:132px;width:717px;height:297px;background:linear-gradient(100deg,#dcecf4 0%,#eaf3f7 35%,#e9cdbb 62%,#d8a98e 80%,#f1f1f0 100%)}
.hero-title{left:60px;top:229px;width:334px;height:57px;background:var(--white);color:var(--sky);font-size:27px;font-weight:400;line-height:57px;padding-left:13px}
.hero-text{left:60px;top:295px;width:389px;height:37px;background:#858585;color:var(--white);font-family:"Arimo",sans-serif;font-size:8.3px;line-height:12px;padding:6px 13px}

/* services */
.services{left:0;top:429px;width:717px;height:189px;background:var(--aqua)}
.service{position:absolute;top:32px;width:160px;text-align:center;color:#222}
.service-icon{width:88px;height:88px;margin:0 auto;border-radius:50%;background:var(--sky);position:relative}
.service-icon::before{content:"";position:absolute;left:0;top:0;width:88px;height:80px;border-radius:50%;background:var(--white)}
.service-icon svg{position:relative;margin-top:22px}
.service h3{font-weight:400;font-size:15.5px;margin-top:5px;letter-spacing:.3px}
.service a{display:block;color:var(--white);font-size:9.5px;text-decoration:none;margin-top:3px;letter-spacing:.3px}

/* about */
.about-band{left:0;top:618px;width:717px;height:289px;background:linear-gradient(90deg,#f7f8fa,#eef2f5 50%,#f3ece8 80%,#f7f8fa)}
.eyebrow{font-size:12.5px;color:var(--sky);font-weight:400}
.heading{font-size:16px;color:#333;font-weight:400;letter-spacing:.3px}
.doctor-photo{left:60px;top:694px;width:145px;height:213px;background:linear-gradient(180deg,#e9ecef,#c9d3dc 50%,#7d8b97);border-radius:40px 40px 0 0}
.about-copy{left:210px;top:708px;width:195px;font-size:8.6px;line-height:13.5px;color:var(--body)}
.bullets{left:210px;top:806px;list-style:none;font-size:7.5px;line-height:13px;color:var(--body)}
.bullets li::before{content:"→";color:#999;margin-right:6px;font-size:7px}
.divider-v{width:1px;background:var(--line)}
.case-photo{top:694px;width:104px;height:83px;border-radius:3px}
.arrows{left:640px;top:662px;font-size:14px;color:#333;letter-spacing:-1px}
.view-all{font-size:9px;color:#333;font-weight:600;letter-spacing:.3px}
.case-copy{left:436px;top:820px;width:222px;font-size:8.6px;line-height:13.3px;color:var(--body)}

/* unique / testimonial */
.step{left:60px;width:230px;height:26px}
.step-num{position:absolute;left:0;top:0;width:25px;height:25px;border-radius:50%;color:var(--white);font-size:12px;line-height:25px;text-align:center}
.step p{position:absolute;left:33px;top:0;width:200px;font-size:8.6px;line-height:12.5px;color:var(--body)}
.rule{height:1px;background:#eee}
.quote-mark{left:322px;top:985px;font-size:62px;font-weight:300;color:#ccc;line-height:1}
.avatar{left:345px;top:1006px;width:52px;height:43px;border:1px solid #ddd;background:linear-gradient(180deg,#e7e2dc,#6b5142 60%,#efeae4)}
.testimonial-copy{left:402px;top:1001px;width:264px;font-size:8.6px;line-height:13px;color:var(--body)}

/* footer */
.footer{left:0;top:1135px;width:717px;height:65px;background:var(--footer)}
.footer-links{left:59px;top:1153px;font-family:"Arimo",sans-serif;font-size:8px;font-weight:700;color:var(--white)}
.footer-links span{margin:0 6px}
.copyright{left:60px;top:1171px;font-family:"Arimo",sans-serif;font-size:8.5px;color:var(--white)}
.footer-name{left:468px;top:1156px;width:190px;text-align:right;font-size:17px;font-weight:400;line-height:22px;color:var(--white);white-space:nowrap}
</style>
</head>
<body>
<div class="page">

  <!-- header -->
  <div class="abs promo">
    <div class="promo-product left" role="img" aria-label="Amber pump bottle of skincare lotion"></div>
    <div class="promo-title">Transform Your Skin To A More<br>Youthful Appearance</div>
    <div class="promo-btn">Read More</div>
    <div class="promo-price">Peptide Renewal Serum<br>$12 (Save 52%)</div>
    <div class="promo-product right" role="img" aria-label="Slim silver serum tube"></div>
  </div>

  <div class="abs social"><span></span><span></span><span></span><span></span></div>
  <div class="abs clinic-name">Brightlumera Skin Clinic</div>

  <nav class="abs nav">
    <a href="#">Home</a><a href="#">About us</a><a href="#">Treatements</a><a href="#">Products</a><a href="#">Results</a><a href="#">Media</a><a href="#">Skin Coditions</a>
  </nav>

  <!-- hero -->
  <div class="abs hero" role="img" aria-label="Woman resting her head on a white towel during a spa skin treatment"></div>
  <h1 class="abs hero-title">SPECIAL CARE SOLUTIONS</h1>
  <p class="abs hero-text">simply dummy text of the printing and typesetting industry. Lorem Ipsum has been the industry's standard dummy text ever since the 1500s, when an unknown printer.</p>

  <!-- services -->
  <section class="abs services">
    <div class="service" style="left:81px">
      <div class="service-icon">
        <svg width="36" height="36" viewBox="0 0 36 36"><rect x="3" y="6" width="30" height="27" rx="3" fill="none" stroke="#444" stroke-width="3"/><rect x="3" y="6" width="30" height="7" fill="#444"/><rect x="9" y="2" width="3" height="8" fill="#444"/><rect x="24" y="2" width="3" height="8" fill="#444"/><text x="18" y="29" font-family="Arimo,sans-serif" font-size="12" font-weight="700" fill="#444" text-anchor="middle">23</text></svg>
      </div>
      <h3>Free Consultation</h3>
      <a href="#">READ MORE »</a>
    </div>
    <div class="service" style="left:256px">
      <div class="service-icon">
        <svg width="36" height="36" viewBox="0 0 36 36"><rect x="13" y="3" width="10" height="6" rx="1" fill="none" stroke="#444" stroke-width="3"/><rect x="2" y="9" width="32" height="24" rx="3" fill="#444"/><rect x="15.5" y="14" width="5" height="14" fill="#fff"/><rect x="11" y="18.5" width="14" height="5" fill="#fff"/></svg>
      </div>
      <h3>Online Products</h3>
      <a href="#">READ MORE »</a>
    </div>
    <div class="service" style="left:449px">
      <div class="service-icon">
        <svg width="36" height="36" viewBox="0 0 36 36"><path d="M7 3v10a7 7 0 0 0 14 0V3" fill="none" stroke="#333" stroke-width="2.5"/><path d="M14 20v6a6 6 0 0 0 12 0v-6" fill="none" stroke="#333" stroke-width="2.5"/><circle cx="27" cy="17" r="4" fill="#fff" stroke="var(--aqua)" stroke-width="3"/></svg>
      </div>
      <h3>Practitioners</h3>
      <a href="#">READ MORE »</a>
    </div>
  </section>

  <!-- about -->
  <div class="abs about-band"></div>
  <div class="abs eyebrow" style="left:78px;top:637px">About</div>
  <h2 class="abs heading" style="left:78px;top:656px">Dr. Adrian Colvey</h2>
  <div class="abs doctor-photo" role="img" aria-label="Smiling doctor in white coat with stethoscope holding a clipboard"></div>
  <p class="abs about-copy">Simply dummy text of the printing and typesetting industry. Lorem Ipsum has been the industry's standard dummy text ever since the 1500s, when an unknown printer took a galley of type and scrambled it to make a type specimen book. It has survived not only five centuries.It was popularised in the 1960s with the release of Letraset.</p>
  <ul class="abs bullets">
    <li>Donec vulputate et nisl a scelerisque .</li>
    <li>Nullam eros arcu, imperdiet eget magna sit amet.</li>
    <li>Curabitur metus nunc, varius eu velit et, lobortis .</li>
    <li>Morbi mi justo, interdum sit amet orci nec..</li>
    <li>Donec vulputate et nisl a scelerisque .</li>
    <li>Nullam eros arcu, imperdiet eget magna sit amet.</li>
  </ul>
  <div class="abs divider-v" style="left:413px;top:650px;height:240px"></div>

  <div class="abs eyebrow" style="left:434px;top:643px">View</div>
  <h2 class="abs heading" style="left:434px;top:662px">Case Studies</h2>
  <div class="abs arrows">‹ ›</div>
  <div class="abs case-photo" style="left:434px;background:linear-gradient(90deg,#c88d6c,#e2b495 48%,#fff 49%,#fff 51%,#e8c2a4 52%,#d9a385)" role="img" aria-label="Before and after photos of facial skin treatment"></div>
  <div class="abs case-photo" style="left:551px;background:linear-gradient(90deg,#d9a08c,#c9786a 48%,#fff 49%,#fff 51%,#e8c5b3 52%,#34507a)" role="img" aria-label="Before and after photos of acne treatment"></div>
  <div class="abs view-all" style="left:618px;top:789px">View All</div>
  <p class="abs case-copy">Simply dummy text of the printing and typesetting industry. Lorem Ipsum has been the industry's standard dummy text ever since the 1500s, when an unknown printer took a galley of type and scrambled.</p>

  <!-- unique -->
  <div class="abs eyebrow" style="left:62px;top:946px">What's Unique</div>
  <h2 class="abs heading" style="left:62px;top:965px">About Our Treatment Protcols</h2>
  <div class="abs step" style="top:996px">
    <span class="step-num" style="background:var(--sky)">1</span>
    <p>Simply dummy text of the printing and typesetting industry. Lorem Ipsum has been the industry's</p>
  </div>
  <div class="abs rule" style="left:60px;top:1032px;width:230px"></div>
  <div class="abs step" style="top:1043px">
    <span class="step-num" style="background:var(--aqua)">2</span>
    <p>Dummy text of the printing and typesetting industry. Lorem Ipsum has been the industry's</p>
  </div>
  <div class="abs view-all" style="left:66px;top:1077px">View All</div>
  <div class="abs divider-v" style="left:309px;top:938px;height:172px"></div>

  <!-- testimonial -->
  <div class="abs eyebrow" style="left:336px;top:946px">Client's</div>
  <h2 class="abs heading" style="left:336px;top:965px">Testimonial</h2>
  <div class="abs quote-mark">{</div>
  <div class="abs avatar" role="img" aria-label="Portrait of a smiling client"></div>
  <p class="abs testimonial-copy">Simply dummy text of the printing and typesetting industry. Lorem Ipsum has been the industry's standard dummy text ever since the 1500s, when an unknown printer took a galley of type and scrambled it to make a type specimen book. It has survived not only five centuries.It was popularised in the 1960s with the release of Letraset.</p>
  <div class="abs view-all" style="left:347px;top:1080px">View All</div>

  <!-- footer -->
  <footer class="abs footer"></footer>
  <div class="abs footer-links">Home<span>|</span>About Us<span>|</span>Treatments<span>|</span>Our services<span>|</span>Our Products</div>
  <div class="abs copyright">© 2015 Brightlumera. All rights reserved.</div>
  <div class="abs footer-name">Brightlumera Skin Clinic</div>

</div>
</body>
</html>
```